Copperkettle Menu

I want to re design my menu at our restaurant Copperkettle, the current menu and information about the restaurant is online at www.copperkettle-eatery.example.nz, have attached the logo for Copperkettle as well as the new menu specifications

Menu design Specifications
· Rustic

· Raw

· Unpolished

· Urban

```html
<!DOCTYPE html>
<html lang="en">
<head>
<meta charset="utf-8">
<title>Copperkettle Eatery &amp; Bar – Menu</title>
<link rel="stylesheet" href="https://fonts.googleapis.com/css2?family=Cormorant+Infant:ital,wght@1,600&family=Arimo:ital,wght@0,400;0,700;1,400&display=swap">
<style>
  :root {
    --wood-dark: #4a2f22;
    --wood-mid: #7a5a46;
    --wood-light: #9a7c66;
    --panel: rgba(236, 233, 230, 0.9);
    --menu-red: #8e1d27;
    --title-blue: #0f4f9c;
    --banner-red: #7c161d;
    --white: #ffffff;
  }
  html, body { margin: 0; padding: 0; overflow: hidden; }
  body { background: #2a1a12; }
  .menu {
    position: relative;
    width: 887px;
    height: 1200px;
    overflow: hidden;
    font-family: "Arimo", Arial, sans-serif;
  }
  .wood {
    position: absolute; inset: 0;
    background:
      linear-gradient(90deg, rgba(0,0,0,0.08) 0 2px, transparent 2px 100%) 0 0 / 74px 100%,
      linear-gradient(180deg, var(--wood-light) 0%, var(--wood-mid) 55%, var(--wood-dark) 100%);
  }
  .panel {
    position: absolute; left: 25px; top: 25px; width: 835px; height: 850px;
    background: var(--panel);
  }
  .section-title {
    position: absolute; left: 48px; margin: 0;
    font-family: "Cormorant Infant", Georgia, serif;
    font-style: italic; font-weight: 600;
    font-size: 66px; line-height: 1; letter-spacing: 2px;
    color: var(--title-blue);
  }
  .section-rule { position: absolute; left: 46px; width: 765px; height: 24px; }
  .col-head {
    position: absolute; top: 121px;
    font-weight: 700; font-size: 21px; color: var(--title-blue);
  }
  .row {
    position: absolute; left: 47px; width: 691px;
    display: flex; align-items: baseline;
    font-size: 20.5px; color: var(--menu-red); white-space: nowrap;
  }
  .leader { flex: 1; border-bottom: 2px dotted var(--menu-red); margin: 0 3px 0 2px; transform: translateY(-4px); }
  .price-one { width: 42px; text-align: right; }
  .price-two { width: 71px; text-align: right; }
  .price { text-align: right; }
  .row-note {
    position: absolute; left: 49px;
    font-size: 20.5px; color: var(--menu-red);
  }
  .banner {
    position: absolute; left: 26px; top: 918px; width: 832px; height: 72px;
    border-radius: 24px; background: var(--banner-red);
    display: flex; align-items: center; justify-content: center;
    color: var(--white); font-style: italic; font-size: 40px; letter-spacing: 0.5px;
  }
  .address {
    position: absolute; left: 45px; top: 1013px;
    color: var(--white); font-size: 20px; line-height: 27px;
  }
  .address p { margin: 0 0 9px; }
  .contact {
    position: absolute; right: 77px; top: 1003px;
    color: var(--white); text-align: right;
  }
  .contact .big { font-size: 35px; line-height: 44px; }
  .contact .small { font-size: 19px; line-height: 29px; margin-right: -14px; }
  .contact .label { margin-right: 18px; }
</style>
</head>
<body>
<main class="menu">
  <div class="wood" role="img" aria-label="Weathered vertical timber planks background"></div>

  <section class="panel" aria-label="Menu"></section>

  <!-- Boards -->
  <h2 class="section-title" style="top:33px;">Boards + two sides</h2>
  <svg class="section-rule" style="top:87px;" viewBox="0 0 765 24"><line x1="0" y1="12" x2="752" y2="12" stroke="#8e1d27" stroke-width="3"/><circle cx="752" cy="12" r="11" fill="#0f4f9c"/></svg>
  <div class="col-head" style="left:584px;">for ONE</div>
  <div class="col-head" style="left:688px;">TWO</div>

  <div class="row" style="top:147px;"><span>Beef wellington &amp; red wine jus</span><span class="leader"></span><span class="price-one">$36</span><span class="price-two">$69</span></div>
  <div class="row" style="top:182px;"><span>Apricot glazed chicken crown</span><span class="leader"></span><span class="price-one">$34</span><span class="price-two">$65</span></div>
  <div class="row" style="top:219px;"><span>Roast Pork scotch &amp; caramelised apple sauce</span><span class="leader"></span><span class="price-one">$32</span><span class="price-two">$60</span></div>
  <div class="row" style="top:253px;"><span>Pan fried line caught fish &amp; lemon pickle</span><span class="leader"></span><span class="price-one">$35</span><span class="price-two">$67</span></div>
  <div class="row" style="top:289px;"><span>Grilled lamb rack &amp; mint sauce</span><span class="leader"></span><span class="price-one">$38</span><span class="price-two">$72</span></div>
  <div class="row" style="top:324px;"><span>Mixed roast nut loaf &amp; rhubarb marmalade</span><span class="leader"></span><span class="price-one">$28</span><span class="price-two">$58</span></div>

  <!-- Sweets -->
  <h2 class="section-title" style="top:369px;">Sweets</h2>
  <svg class="section-rule" style="top:422px;" viewBox="0 0 765 24"><line x1="0" y1="12" x2="752" y2="12" stroke="#8e1d27" stroke-width="3"/><circle cx="752" cy="12" r="11" fill="#0f4f9c"/></svg>

  <div class="row" style="top:455px;"><span>Orange pannacotta with earl grey &amp; cardamom syrup</span><span class="leader"></span><span class="price">$12</span></div>
  <div class="row-note" style="top:488px;">Chocolate terrine, macerated strawberries &amp; macadamia</div>
  <div class="row" style="top:517px;"><span>mascarpone</span><span class="leader"></span><span class="price">$14</span></div>
  <div class="row" style="top:548px;"><span>Vanilla bean crème brulee with cranberry &amp; pistachio biscotti</span><span class="leader"></span><span class="price">$12</span></div>
  <div class="row" style="top:585px;"><span>Pavolva roulade, kiwifruit, summer berries &amp; passionfruit cream</span><span class="leader"></span><span class="price">$12</span></div>

  <!-- Cheese -->
  <h2 class="section-title" style="top:632px;">Cheese</h2>
  <svg class="section-rule" style="top:686px;" viewBox="0 0 765 24"><line x1="0" y1="12" x2="752" y2="12" stroke="#8e1d27" stroke-width="3"/><circle cx="752" cy="12" r="11" fill="#0f4f9c"/></svg>

  <div class="row" style="top:718px;"><span>Riverstone aged cheddar</span><span class="leader"></span><span class="price">$16</span></div>
  <div class="row" style="top:751px;"><span>High pasture triple Brie</span><span class="leader"></span><span class="price">$18</span></div>
  <div class="row-note" style="top:783px;">Harbour Blue</div>
  <div class="row" style="top:812px;"><span>with dried fruit, nuts, fruit paste and wafers</span><span class="leader"></span><span class="price">$14</span></div>

  <div class="banner">OPEN FROM 3PM TUESDAY TO SUNDAY</div>

  <address class="address" style="font-style:normal;">
    <p>Copperkettle Eatery &amp; Bar<br>PO Box 10482, Wellington</p>
    <p>18 Lantern Place (corner<br>of Mercer Lane &amp; Lantern Place)<br>Wellington 6011</p>
  </address>

  <div class="contact">
    <div class="big">phone +64 4 555 0136</div>
    <div class="big">fax : +64 4 555 0139</div>
    <div class="small"><span class="label">e-mail :</span>info@copperkettle-eatery.example.nz</div>
    <div class="small"><span class="label">website :</span>www.copperkettle-eatery.example.nz</div>
  </div>
</main>
</body>
</html>
```